Stationery for new photography studio
Flyer, Gift Certificate, Business Card, headed paper, CD label and case cover
Please note the change in email address
studio@brightferndesigns.at
Dear sir,
Thanks for your feedback.
#100 is brilliant
I really like #97. I love the colours from the photos. I like the new business cards. Could you combine the concepts in the business cards from #94 #96 #97
temp web address
http://brightferndesigns.snapvault-host.com/
#89 every thing looks great. A few comments:
1) The business cards - I like the logo side however the information side I prefer earlier designs where you used one block colour ie- #87 or #49. I'm still not sure about this side.
2) The dark black logo square on the paper looks too bold.
Great work. Thanks a lot.
Please check the newly uploaded files.
PANTONES:
Blue: 310 C
Brown: 409 C
Pink: 211 C
Gray: 424 C
FONTS:
Petra: Gotham Medium
Valkenor: Gotham Book
Tagline: Gotham Book
Signature: Custom made
I think I prefer the logo in #52 where it is slightly off the page than #70 where it is completely visible.
I like #70, it's sophisticated however the colour scheme is starting depart from the original and from the style of my work, which I think is not so heavy.
If you have any change or better suggestions please let me know.
Thank you.
#61 - #64 I'm not sure if the dots down the sides are necessary.
My website is down. But I'LL let you know when it's back up so you can take a look at some more pictures. I love the use of them in your designs. So excited by what I'm seeing. Thanks for your work so far.
#57. I love it. Everything adds up perfectly. Not sure about the font. It's a bit clumsy. I'd like something sharper and sleeker.
Great direction.
Does this work for A6
A CD disk is 120 mm in diameter (60 mm radius), with a hole 15 mm diameter (7.5 mm radius)
I'm looking on google for CD dimensions. So far I've found the case cover dimensions:
CD Cover Size Specifications for Printing
The finished dimensions for the outside of printed CD covers are 4.724 inches square. Many printed designs include bleed. The "bleed area" is an extra 1/8" of space for design elements or backgrounds to extend beyond the finished size of your piece. A CD cover with bleeds is printed slightly oversized (4.974 inches square) and then cut down to size, giving the appearance that the printing "bleeds" off the edge of the cover rather than having a white border.
Really like the direction of #51 and #52. Re. #55 I prefer the designs where all embellishments or lines are relevant. What I mean by this is that the curve does not tie in anywhere. It's an additional form that is not part of the logo.
#61 and #62 are great. Can you show me some alternative fonts for the 15% and the brightferndesigns.at
This is fun project! What size should be the CD label be? I am not too sure!
#36 with black background?
I'd be interested to see #34 with black replacing the pink.
I have uploaded information to be included in the flyers and gift certificate.
Please look at my photos to understand my style
http://www.facebook.com/BrightFern.Designs?sk=app_274930158846320

```html
<!DOCTYPE html>
<html lang="de">
<head>
<meta charset="utf-8">
<title>Petra Valkenor – Business Card</title>
<link rel="stylesheet" href="https://fonts.googleapis.com/css2?family=Montserrat:wght@400;500;600&display=swap">
<style>
  :root {
    --pink: #f08fb2;
    --pink-deep: #ea7aa3;
    --white: #ffffff;
    --grey-text: #6d6d72;
    --ink: #3d3d42;
    --backdrop: #e7e5e2;
  }
  * { box-sizing: border-box; margin: 0; padding: 0; }
  html, body {
    width: 1200px; height: 850px; overflow: hidden;
    background: var(--backdrop);
    font-family: "Montserrat", Arial, sans-serif;
  }
  .stage { position: relative; width: 1200px; height: 850px; }

  .card {
    position: absolute;
    width: 620px; height: 355px;
    border-radius: 34px;
    overflow: hidden;
    box-shadow: 0 10px 30px rgba(0,0,0,0.12);
  }

  /* information side */
  .card--info { left: 60px; top: 60px; background: var(--white); }
  .card--info .sweep { position: absolute; inset: 0; }
  .brand { position: absolute; left: 46px; top: 40px; }
  .brand-mark {
    width: 34px; height: 34px; border-radius: 50%;
    border: 3px solid var(--pink); margin: 0 0 10px 80px;
  }
  .brand-name {
    font-size: 31px; font-weight: 400; letter-spacing: 3px;
    color: var(--grey-text); white-space: nowrap;
  }
  .brand-tagline {
    margin-top: 4px; margin-left: 64px;
    font-size: 10px; letter-spacing: 3.4px; color: var(--pink);
    text-transform: uppercase;
  }
  .contact { position: absolute; left: 46px; top: 212px; color: var(--ink); font-size: 13.5px; line-height: 19px; }
  .contact-name { font-size: 19px; font-weight: 600; color: var(--pink); margin-bottom: 3px; }
  .contact-label { color: var(--pink); display: inline-block; width: 16px; }

  /* logo side */
  .card--logo { left: 520px; top: 440px; background: var(--pink); }
  .logo-lockup { position: absolute; left: 0; right: 0; top: 88px; text-align: center; color: var(--white); }
  .logo-lockup .brand-mark { border-color: var(--white); width: 52px; height: 52px; margin: 0 auto 18px; border-width: 4px; }
  .logo-lockup .brand-name { font-size: 44px; letter-spacing: 5px; color: var(--white); font-weight: 500; }
  .logo-lockup .brand-tagline { margin: 8px 0 0; font-size: 13px; letter-spacing: 6px; color: var(--white); }
</style>
</head>
<body>
<main class="stage">

  <section class="card card--info" aria-label="Business card, information side">
    <svg class="sweep" viewBox="0 0 620 355" preserveAspectRatio="none" aria-hidden="true">
      <path d="M520 0 C 420 70, 440 260, 250 355 L 620 355 L 620 0 Z" fill="var(--pink)"/>
    </svg>
    <div class="brand">
      <div class="brand-mark"></div>
      <p class="brand-name">Petra Valkenor</p>
      <p class="brand-tagline">Bright &amp; Fern Designs</p>
    </div>
    <address class="contact" style="font-style:normal">
      <p class="contact-name">Petra Valkenor</p>
      <p>Lindenweg 14/3</p>
      <p>1050 Wien</p>
      <p><span class="contact-label">p:</span>06641287354</p>
      <p><span class="contact-label">e:</span>Petra@Valkenor.at</p>
      <p>www.BrightFernDesigns.at</p>
    </address>
  </section>

  <section class="card card--logo" aria-label="Business card, logo side">
    <div class="logo-lockup">
      <div class="brand-mark"></div>
      <p class="brand-name">Petra Valkenor</p>
      <p class="brand-tagline">Bright Fern Designs</p>
    </div>
  </section>

</main>
</body>
</html>
```